Create Premium Wine Label Design

We are premium wine exporters from Australia. We are looking to introduce new brand " The Velloran" - in red wine, White wine and Sparkling wine to international market.

The sample label design for red wine ( Shiraz) is attached.

This is our luxury brand. We need a stunning wine label designs for (front, back and neck) that should be mostly in GOLD colour and design should be really eye catching.

We have provided sample design for front, back and neck labels. However, we are looking forward to see a completely new improvised design.

LOGO attached.

Front Label Design Specification:

* We would like to see designs that are in Gold colour.
* Wine Bottle size is standard: 750ml; we assume the same design can be resizable to different bottle sizes.
* Our design should suit both black, white and sparkling wine bottles(sample attached)
* Use our logo in the design (see attached - label sample)
* Content for front label (see attached).
* Design should include all information specified in the sample

Back Label Design
* All contents in the sample should be used ( sample attached)
* LOGO attached.

Neck Label Design
* Sample of Neck label attached, please provide similar or your own design.
* LOGO attached.

Image Samples:
* Samples of label designs we like (see attached)
* Sample for gold color (see attached)
* For bottle shapes (see attached)
* Front, Back and Neck Label Samples (see attached)

Target Market(s)

International Wine Market

Font styles to use
Decorative
Script

Requirements
Must have
• Must have golden color on front and back label

```html
<!DOCTYPE html>
<html lang="en">
<head>
<meta charset="utf-8">
<title>Meridale Shiraz – Label Set</title>
<link rel="stylesheet" href="https://fonts.googleapis.com/css2?family=Cinzel:wght@500&family=Lobster&family=Oswald:wght@300;400;500&family=Poiret+One&family=Roboto:wght@400&display=swap">
<style>
  :root{
    --label-black:#0b0b0b;
    --gold-light:#f6dc8c;
    --gold:#d9a938;
    --gold-deep:#8a5a12;
    --wine-red:#c5121a;
    --wine-dark:#5a0508;
    --paper:#ffffff;
    --ink-dark:#1a1205;
  }
  *{margin:0;padding:0;box-sizing:border-box}
  html,body{width:1200px;height:1114px;overflow:hidden;background:var(--paper)}
  .canvas{position:relative;width:1200px;height:1114px}

  .label{position:absolute;background:var(--label-black);overflow:hidden}
  .front-label{left:18px;top:40px;width:318px;height:476px}
  .back-label{left:360px;top:40px;width:318px;height:476px}

  .title-art{position:absolute;left:0;top:0;width:318px;height:476px}
  .varietal{font-family:'Oswald',sans-serif;font-weight:300}
  .cuvee{font-family:'Lobster',cursive}
  .vintage{font-family:'Oswald',sans-serif;font-weight:500}

  .brand-name{
    position:absolute;font-family:'Cinzel',serif;font-weight:500;color:var(--gold);
    letter-spacing:1px;text-align:center;white-space:nowrap
  }

  /* front */
  .front-label .brand-name{left:0;width:318px;top:72px;font-size:20px}
  .origin{
    position:absolute;left:0;width:318px;top:437px;text-align:center;
    font-family:'Poiret One',sans-serif;font-size:15px;color:var(--gold);letter-spacing:.5px
  }

  /* back */
  .tasting-panel{
    position:absolute;left:12px;top:188px;width:294px;height:133px;border-radius:12px;
    border:2px solid var(--gold);overflow:hidden;background:var(--label-black)
  }
  .tasting-notes{
    height:88px;padding:5px 6px;text-align:center;font-family:'Roboto',sans-serif;
    font-size:9.6px;line-height:13px;color:var(--ink-dark);
    background:linear-gradient(180deg,var(--gold-deep),var(--gold) 30%,var(--gold-light) 55%,var(--gold) 80%,var(--gold-deep))
  }
  .producer-notes{
    padding:5px 8px;text-align:center;font-family:'Roboto',sans-serif;font-size:7px;line-height:9.5px;color:#f1f1f1
  }
  .product-badge{
    position:absolute;left:74px;top:321px;width:168px;height:23px;border-radius:4px;
    border:1px solid var(--gold-deep);
    background:linear-gradient(180deg,var(--gold-light),var(--gold) 50%,var(--gold-deep));
    font-family:'Oswald',sans-serif;font-size:15px;line-height:21px;text-align:center;color:var(--ink-dark)
  }
  .barcode-space{position:absolute;left:15px;top:358px;width:181px;height:98px;background:var(--paper)}
  .legal-text{
    position:absolute;left:204px;top:358px;width:108px;text-align:center;
    font-family:'Roboto',sans-serif;font-size:7px;line-height:9px;color:var(--gold)
  }
  .back-label .brand-name{left:210px;width:96px;top:435px;font-size:10px}

  /* neck */
  .neck-label{position:absolute;left:693px;top:162px;width:477px;height:195px;background:var(--paper)}
  .gold-band{
    position:absolute;left:0;width:477px;
    background:linear-gradient(180deg,var(--gold-deep),var(--gold) 25%,var(--gold-light) 50%,var(--gold) 75%,var(--gold-deep))
  }
  .neck-black{position:absolute;left:0;width:477px;background:var(--label-black)}
  .neck-label .brand-name{top:74px;font-size:22px;width:170px}
  .brand-dot{position:absolute;left:226px;top:79px;width:24px;height:24px;border-radius:50%;background:var(--gold)}
</style>
</head>
<body>
<main class="canvas">

  <section class="label front-label" aria-label="Front label">
    <div class="brand-name">MERIDALE</div>
    <svg class="title-art" viewBox="0 0 318 476" aria-label="Shiraz, the Velloran, 2018">
      <defs>
        <linearGradient id="frontGold" x1="0" y1="0" x2="0" y2="1">
          <stop offset="0" stop-color="#f6dc8c"/><stop offset=".45" stop-color="#d9a938"/><stop offset="1" stop-color="#8a5a12"/>
        </linearGradient>
        <linearGradient id="frontRed" x1="0" y1="0" x2="0" y2="1">
          <stop offset="0" stop-color="#ff3b35"/><stop offset=".5" stop-color="#c5121a"/><stop offset="1" stop-color="#5a0508"/>
        </linearGradient>
      </defs>
      <text class="varietal" x="47" y="300" font-size="170" textLength="197" lengthAdjust="spacingAndGlyphs" fill="url(#frontGold)">SHIRAZ</text>
      <text class="cuvee" x="92" y="338" font-size="52" textLength="185" lengthAdjust="spacingAndGlyphs" fill="url(#frontRed)">the Velloran</text>
      <text class="vintage" x="182" y="352" font-size="24" textLength="54" lengthAdjust="spacingAndGlyphs" fill="url(#frontGold)">2018</text>
    </svg>
    <div class="origin">WINE OF AUSTRALIA</div>
  </section>

  <section class="label back-label" aria-label="Back label">
    <svg class="title-art" viewBox="0 0 318 476" aria-label="Shiraz, the Velloran, 2018">
      <defs>
        <linearGradient id="backGold" x1="0" y1="0" x2="0" y2="1">
          <stop offset="0" stop-color="#f6dc8c"/><stop offset=".45" stop-color="#d9a938"/><stop offset="1" stop-color="#8a5a12"/>
        </linearGradient>
        <linearGradient id="backRed" x1="0" y1="0" x2="0" y2="1">
          <stop offset="0" stop-color="#ff3b35"/><stop offset=".5" stop-color="#c5121a"/><stop offset="1" stop-color="#5a0508"/>
        </linearGradient>
      </defs>
      <text class="varietal" x="68" y="120" font-size="125" textLength="162" lengthAdjust="spacingAndGlyphs" fill="url(#backGold)">SHIRAZ</text>
      <text class="cuvee" x="105" y="160" font-size="40" textLength="150" lengthAdjust="spacingAndGlyphs" fill="url(#backRed)">the Velloran</text>
      <text class="vintage" x="175" y="173" font-size="16" textLength="46" lengthAdjust="spacingAndGlyphs" fill="url(#backGold)">2018</text>
    </svg>
    <div class="tasting-panel">
      <p class="tasting-notes">Lorem ipsum dolor sit amet, consectetuer adipiscing elit, sed diam nonummy nibh euismod tincidunt ut laoreet dolore magna aliquam erat volutpat. Lorem ipsum dolor sit amet, consectetuer adipiscing elit, sed diam nonummy nibh euismod tincidunt ut laoreet dolore magna aliquam erat volutpat. Lorem ipsum dolor sit amet, consectetuer adipiscing.</p>
      <p class="producer-notes">Lorem ipsum dolor sit amet, consectetuer adipiscing elit, sed diam nonummy nibh euismod tincidunt ut laoreet dolore magna aliquam erat volutpat. Ut wisi enim ad minim veniam,</p>
    </div>
    <div class="product-badge">PRODUCT OF AUSTRALIA</div>
    <div class="barcode-space"></div>
    <p class="legal-text">Lorem ipsum dolor sit amet, consectetuer adipiscing elit, sed diam nonummy nibh euismod tincidunt ut laoreet dolore magna aliquam erat</p>
    <div class="brand-name">MERIDALE</div>
  </section>

  <section class="neck-label" aria-label="Neck label">
    <div class="gold-band" style="top:0;height:20px"></div>
    <div class="neck-black" style="top:20px;height:10px"></div>
    <div class="gold-band" style="top:30px;height:22px"></div>
    <div class="neck-black" style="top:56px;height:82px"></div>
    <div class="brand-name" style="left:12px">MERIDALE</div>
    <div class="brand-dot"></div>
    <div class="brand-name" style="left:290px">MERIDALE</div>
    <div class="gold-band" style="top:142px;height:22px"></div>
    <div class="neck-black" style="top:164px;height:10px"></div>
    <div class="gold-band" style="top:174px;height:21px"></div>
  </section>

</main>
</body>
</html>
```